BRIMWAVE.live*

I am needing a web site built for the main purpose of uploading podcasts
(MP3 files) to be viewed by large audiences of 1000+ site visitors on a regular basis. I have created a rough draft of how I want the site to look.

i have created a rough draft of the home page - the LOGO for this site is a spectacular lightening bolt which appears on my home page sample... the file for this image I purchased is too large to download to your site. I will supply on reuquest.

There will be 5 pages; HOME ABOUT RESOURCES DEVOTIONALS MORTY.
I have all the content prepared for each of the above pages.

Target Market(s)

All people groups seeking positive and encouraging words, life lessons and testimonies of faith.

Coding

Coded - Design and coding required

Number of Pages Required

1 page

Colors
3176b5

Requirements
Must have
• The design and layout provided - my sample

Black backgrounds as shown on my sample

```html
<!DOCTYPE html>
<html lang="en">
<head>
<meta charset="utf-8">
<title>BRIMWAVE.live — Life Changing Podcasts</title>
<link rel="stylesheet" href="https://fonts.googleapis.com/css2?family=Abril+Fatface&family=Lato:wght@400;700&display=swap">
<style>
:root{
  --brand:#3176b5;
  --night:#020a2a;
  --deep:#0a2a7a;
  --black:#050505;
  --white:#ffffff;
  --disc-red:#c8101e;
}
*{margin:0;padding:0;box-sizing:border-box}
html,body{width:1200px;height:1092px;overflow:hidden;background:var(--black)}
body{position:relative;font-family:'Lato',sans-serif;color:var(--white)}
.hero{position:absolute;left:0;top:0;width:1200px;height:584px;
  background:radial-gradient(ellipse at 40% 45%,#0b3aa8 0%,#06206a 30%,var(--night) 65%,#01061c 100%)}
.hero-photo{position:absolute;left:0;top:60px;width:680px;height:524px;
  background:radial-gradient(ellipse at 55% 40%,#1aa6ff 0%,#0a3fb0 30%,#0a1f5a 60%,rgba(2,10,42,0) 85%),
  linear-gradient(180deg,rgba(0,0,0,0) 60%,rgba(120,70,30,.45) 100%)}
.site-nav{position:absolute;top:0;left:0;width:1200px;height:82px}
.site-nav a{position:absolute;top:31px;font-family:'Abril Fatface',serif;font-size:15px;letter-spacing:.5px;color:var(--white);text-decoration:none}
.brand{position:absolute;left:415px;top:10px;font-family:'Abril Fatface',serif;font-size:49px;line-height:1;color:var(--white);letter-spacing:1px}
.brand small{font-size:18px;letter-spacing:0}
.hero-title{position:absolute;left:673px;top:152px;font-family:'Abril Fatface',serif;font-size:60px;line-height:71px;letter-spacing:3px}
.player{position:absolute;left:673px;top:380px;width:429px;height:55px;background:var(--brand);border-radius:2px}
.player .label{position:absolute;left:72px;top:11px;font-size:10px}
.player .time{position:absolute;left:259px;top:11px;font-size:10px}
.player svg{position:absolute;left:0;top:0}
.listen{position:absolute;left:674px;top:463px;font-family:'Abril Fatface',serif;font-size:12px;letter-spacing:.6px}
.listen-icons{position:absolute;left:766px;top:463px}
.episodes{position:absolute;left:0;top:590px;width:1200px;height:286px;display:flex;gap:5px}
.episode{width:236px;height:286px;position:relative}
.episode .art{height:172px}
.episode .body{height:114px;background:var(--brand);text-align:center}
.episode h3{font-family:'Abril Fatface',serif;font-weight:400;font-size:19px;padding-top:28px;letter-spacing:.5px}
.episode p{font-size:12.6px;line-height:22px;margin-top:4px}
.episode .pod{position:absolute;left:98px;top:150px}
.socials{position:absolute;left:533px;top:936px}
.footer-nav{position:absolute;top:988px;left:0;width:1200px;text-align:center;font-family:'Abril Fatface',serif;font-size:15px;letter-spacing:.4px}
.footer-nav span{margin:0 13px}
.copyright{position:absolute;top:1036px;left:0;width:1200px;text-align:center;font-size:16px}
</style>
</head>
<body>
<header class="hero">
  <div class="hero-photo" role="img" aria-label="Host in black t-shirt with arms crossed, seated on a motorcycle, in front of a glowing blue lightning bolt"></div>
  <nav class="site-nav">
    <a href="#" style="left:128px">HOME</a>
    <a href="#" style="left:225px">ABOUT</a>
    <a href="#" style="left:329px">MORTY</a>
    <div class="brand">BRIMWAVE<small>.LIVE</small></div>
    <a href="#" style="left:814px">RESOURCES</a>
    <a href="#" style="left:961px">DEVOTIONALS</a>
  </nav>
  <h1 class="hero-title">LIFE<br>CHANGING<br>PODCASTS</h1>
  <div class="player">
    <svg width="429" height="55" viewBox="0 0 429 55">
      <polygon points="19,19 19,35 33,27" fill="#fff"/>
      <rect x="53" y="19" width="16" height="16" rx="2" fill="#fff"/>
      <line x1="82" y1="36" x2="381" y2="36" stroke="rgba(255,255,255,.4)" stroke-width="1.5"/>
      <circle cx="72" cy="37" r="4" fill="#fff"/>
      <polygon points="338,23 342,23 346,19 346,35 342,31 338,31" fill="#fff"/>
      <path d="M349,23 q3,4 0,8" stroke="#fff" stroke-width="1.5" fill="none"/>
      <line x1="358" y1="27" x2="407" y2="27" stroke="#fff" stroke-width="2"/>
      <circle cx="407" cy="27" r="4.5" fill="#fff"/>
    </svg>
    <span class="label">Lorem Ipsum Sed</span>
    <span class="time">00: 06/07:36</span>
  </div>
  <div class="listen">LISTEN ON</div>
  <svg class="listen-icons" width="70" height="14" viewBox="0 0 70 14" aria-hidden="true">
    <rect x="0" y="2" width="9" height="9" fill="var(--brand)"/>
    <rect x="27" y="2" width="9" height="9" fill="var(--brand)"/>
    <rect x="55" y="2" width="9" height="9" fill="var(--brand)"/>
  </svg>
</header>

<section class="episodes">
  <article class="episode">
    <div class="art" role="img" aria-label="Woman with open arms facing a sunset over mountains" style="background:linear-gradient(180deg,#3d8fa8 0%,#e0b24a 55%,#6b5a3a 100%)"></div>
    <div class="body"><h3>Episode -1</h3><p>Lorem ipsum dolor sit amet, ctetur<br>adipiscing elit, sed do eiusmod</p></div>
    <svg class="pod" width="40" height="44" viewBox="0 0 40 44" aria-hidden="true"><path d="M0,20 A20,20 0 0 1 40,20" fill="var(--disc-red)"/><circle cx="20" cy="22" r="19" fill="var(--brand)"/><circle cx="20" cy="22" r="12" fill="none" stroke="#fff" stroke-width="2.5"/><circle cx="20" cy="22" r="7" fill="none" stroke="#fff" stroke-width="2.5"/><circle cx="20" cy="21" r="3" fill="#fff"/><rect x="18" y="24" width="4" height="12" rx="2" fill="#fff"/></svg>
  </article>
  <article class="episode">
    <div class="art" role="img" aria-label="Man reading a glowing book beneath a tree at dusk" style="background:linear-gradient(180deg,#3f5a6e 0%,#6a7f86 50%,#2e3a36 100%)"></div>
    <div class="body"><h3>Episode -2</h3><p>Lorem ipsum dolor sit amet, ctetur<br>adipiscing elit, sed do eiusmod</p></div>
    <svg class="pod" width="40" height="44" viewBox="0 0 40 44" aria-hidden="true"><path d="M0,20 A20,20 0 0 1 40,20" fill="var(--disc-red)"/><circle cx="20" cy="22" r="19" fill="var(--brand)"/><circle cx="20" cy="22" r="12" fill="none" stroke="#fff" stroke-width="2.5"/><circle cx="20" cy="22" r="7" fill="none" stroke="#fff" stroke-width="2.5"/><circle cx="20" cy="21" r="3" fill="#fff"/><rect x="18" y="24" width="4" height="12" rx="2" fill="#fff"/></svg>
  </article>
  <article class="episode">
    <div class="art" role="img" aria-label="Figure walking a tightrope between two cliffs at sunset" style="background:linear-gradient(180deg,#f0a07a 0%,#e8562a 60%,#7a1c10 100%)"></div>
    <div class="body"><h3>Episode -3</h3><p>Lorem ipsum dolor sit amet, ctetur<br>adipiscing elit, sed do eiusmod</p></div>
    <svg class="pod" width="40" height="44" viewBox="0 0 40 44" aria-hidden="true"><path d="M0,20 A20,20 0 0 1 40,20" fill="var(--disc-red)"/><circle cx="20" cy="22" r="19" fill="var(--brand)"/><circle cx="20" cy="22" r="12" fill="none" stroke="#fff" stroke-width="2.5"/><circle cx="20" cy="22" r="7" fill="none" stroke="#fff" stroke-width="2.5"/><circle cx="20" cy="21" r="3" fill="#fff"/><rect x="18" y="24" width="4" height="12" rx="2" fill="#fff"/></svg>
  </article>
  <article class="episode">
    <div class="art" role="img" aria-label="Coffee cup and pen beside a note of work-life balance words" style="background:linear-gradient(135deg,#8aa4b8 0%,#e8e2d4 45%,#c9bfa8 100%)"></div>
    <div class="body"><h3>Episode -4</h3><p>Lorem ipsum dolor sit amet, ctetur<br>adipiscing elit, sed do eiusmod</p></div>
    <svg class="pod" width="40" height="44" viewBox="0 0 40 44" aria-hidden="true"><path d="M0,20 A20,20 0 0 1 40,20" fill="var(--disc-red)"/><circle cx="20" cy="22" r="19" fill="var(--brand)"/><circle cx="20" cy="22" r="12" fill="none" stroke="#fff" stroke-width="2.5"/><circle cx="20" cy="22" r="7" fill="none" stroke="#fff" stroke-width="2.5"/><circle cx="20" cy="21" r="3" fill="#fff"/><rect x="18" y="24" width="4" height="12" rx="2" fill="#fff"/></svg>
  </article>
  <article class="episode">
    <div class="art" role="img" aria-label="Motivational quote about failure over a lake and sky scene" style="background:linear-gradient(180deg,#9fb2c4 0%,#5f7386 55%,#1e2830 100%)"></div>
    <div class="body"><h3>Episode -5</h3><p>Lorem ipsum dolor sit amet, ctetur<br>adipiscing elit, sed do eiusmod</p></div>
    <svg class="pod" width="40" height="44" viewBox="0 0 40 44" aria-hidden="true"><path d="M0,20 A20,20 0 0 1 40,20" fill="var(--disc-red)"/><circle cx="20" cy="22" r="19" fill="var(--brand)"/><circle cx="20" cy="22" r="12" fill="none" stroke="#fff" stroke-width="2.5"/><circle cx="20" cy="22" r="7" fill="none" stroke="#fff" stroke-width="2.5"/><circle cx="20" cy="21" r="3" fill="#fff"/><rect x="18" y="24" width="4" height="12" rx="2" fill="#fff"/></svg>
  </article>
</section>

<footer>
  <svg class="socials" width="134" height="30" viewBox="0 0 134 30" aria-hidden="true">
    <g fill="none" stroke="#fff" stroke-width="1.2">
      <circle cx="15" cy="15" r="13.5"/><circle cx="50" cy="15" r="13.5"/>
      <circle cx="84" cy="15" r="13.5"/><circle cx="118" cy="15" r="13.5"/>
    </g>
  </svg>
  <nav class="footer-nav">
    <span>HOME</span>|<span>ABOUT&nbsp;&nbsp;&nbsp;MORTY</span>|<span>RESOURCES</span>|<span>DEVOTIONALS</span>
  </nav>
  <p class="copyright">Copyright © 2020 BRIMWAVE.live. All Rights Reserved.</p>
</footer>
</body>
</html>
```